Real Estate developer

I am building a 55+ adult community and I need a business card
Information to be Included in the Business Card:
Company Name: Birch Hollow Residences, in my font
Temm Boyle
President
Phone: 207-546-1382
Address:
Birch Hollow Residences, LLC
9 Quillfeather Road,
Harlow Falls VERMONT, 05917
Web Address: www.birchhollowresidencesnorth.net
Target Market(s)
55 year and older home buyers
Industry/Entity Type
Building
Font styles to use
Other font styles liked:
- Boulevard BQ
Requirements
Must have
- This message must be on card: A 55+ Adult Community

```html
<!DOCTYPE html>
<html lang="en">
<head>
<meta charset="utf-8">
<title>Birch Hollow Residences – Business Card</title>
<link rel="stylesheet" href="https://fonts.googleapis.com/css2?family=Pinyon+Script&family=Cinzel:wght@600&family=Arimo:wght@400&display=swap">
<style>
  :root {
    --page-bg: #eeeeee;
    --green-dark: #123f2c;
    --green-mid: #1f5e43;
    --green-light: #2c7353;
    --gold: #e2b857;
    --gold-band: #f3b85c;
    --band-ink: #1b1b1b;
    --black: #0b0b0b;
    --charcoal: #1c1c1c;
    --name-green: #3f9a68;
    --icon-green: #3f9a68;
    --white: #ffffff;
  }
  html, body {
    margin: 0;
    width: 1200px;
    height: 900px;
    overflow: hidden;
    background: var(--page-bg);
  }
  .business-card {
    position: absolute;
    left: 100px;
    top: 150px;
    width: 1000px;
    height: 600px;
    border-radius: 42px;
    overflow: hidden;
    background: var(--black);
  }
  .card-header {
    position: absolute;
    inset: 0 0 auto 0;
    height: 255px;
    background: linear-gradient(180deg, var(--green-light) 0%, var(--green-mid) 55%, var(--green-dark) 100%);
  }
  .header-art {
    position: absolute;
    left: 90px;
    right: 60px;
    top: 30px;
    bottom: 0;
    background: linear-gradient(180deg, rgba(255,255,255,0) 0%, rgba(255,255,255,0.07) 60%, rgba(255,255,255,0.03) 100%);
  }
  .company-name {
    position: absolute;
    left: 0;
    right: 0;
    top: 70px;
    margin: 0;
    text-align: center;
    font-family: "Pinyon Script", cursive;
    font-weight: 400;
    font-size: 104px;
    line-height: 1;
    color: var(--gold);
  }
  .tagline {
    position: absolute;
    left: 0;
    right: 0;
    top: 255px;
    height: 26px;
    background: var(--gold-band);
    color: var(--band-ink);
    font-family: "Cinzel", serif;
    font-weight: 600;
    font-size: 22px;
    line-height: 26px;
    letter-spacing: 9px;
    text-align: center;
  }
  .card-body {
    position: absolute;
    left: 0;
    right: 0;
    top: 281px;
    bottom: 0;
  }
  .body-pattern {
    position: absolute;
    inset: 0;
    background: radial-gradient(ellipse at 55% 40%, var(--charcoal) 0%, var(--black) 75%);
  }
  .contact-block {
    position: absolute;
    left: 40px;
    top: 16px;
    font-family: "Arimo", sans-serif;
  }
  .person-name {
    margin: 0;
    font-size: 40px;
    line-height: 46px;
    color: var(--name-green);
    font-weight: 400;
  }
  .person-title {
    margin: 0 0 26px;
    font-size: 36px;
    line-height: 42px;
    color: var(--gold);
  }
  .contact-list {
    list-style: none;
    margin: 0;
    padding: 0;
    color: var(--white);
    font-size: 34px;
    line-height: 40px;
  }
  .contact-item {
    display: flex;
    align-items: flex-start;
    gap: 14px;
  }
  .contact-icon {
    width: 34px;
    height: 34px;
    margin-top: 3px;
    flex: none;
    fill: var(--icon-green);
  }
  .contact-icon.globe {
    fill: none;
    stroke: var(--icon-green);
    stroke-width: 2.5;
  }
  .item-web { margin-top: 4px; }
</style>
</head>
<body>
  <article class="business-card">
    <header class="card-header">
      <div class="header-art" role="img" aria-label="Faint line drawing of a row of homes"></div>
      <h1 class="company-name">Birch Hollow Residences</h1>
    </header>
    <div class="tagline">A 55+ Adult Community</div>
    <section class="card-body">
      <div class="body-pattern" role="img" aria-label="Dark damask pattern background"></div>
      <div class="contact-block">
        <h2 class="person-name">Temm Boyle</h2>
        <p class="person-title">President</p>
        <ul class="contact-list">
          <li class="contact-item">
            <svg class="contact-icon" viewBox="0 0 24 24" aria-hidden="true"><path d="M6.6 10.8a15.1 15.1 0 0 0 6.6 6.6l2.2-2.2a1 1 0 0 1 1-.25 11.4 11.4 0 0 0 3.6.6 1 1 0 0 1 1 1V20a1 1 0 0 1-1 1A17 17 0 0 1 3 4a1 1 0 0 1 1-1h3.5a1 1 0 0 1 1 1c0 1.250.2 2.45.6 3.6a1 1 0 0 1-.25 1z"/></svg>
            <span>207-546-1382</span>
          </li>
          <li class="contact-item">
            <svg class="contact-icon" viewBox="0 0 24 24" aria-hidden="true"><path d="M12 3 1.5 12h3v9h5.5v-6h4v6h5.5v-9h3z"/></svg>
            <span>9 Quillfeather Road,<br>Harlow Falls VERMONT, 05917</span>
          </li>
          <li class="contact-item item-web">
            <svg class="contact-icon globe" viewBox="0 0 24 24" aria-hidden="true"><circle cx="12" cy="12" r="9.5"/><ellipse cx="12" cy="12" rx="4.2" ry="9.5"/><path d="M2.5 12h19M4 7h16M4 17h16"/></svg>
            <span>www.birchhollowresidencesnorth.net</span>
          </li>
        </ul>
      </div>
    </section>
  </article>
</body>
</html>
```